Pamphlet design, flyer, and poster for cardiology office

Hello design experts out there. We are looking for the following:
1. Brochure : accordian Z fold design.
2. Company folder with content (see pamphlet idea and design example.
3. Large pull up poster/banner.

They are used promote our Cardiology office.

The services our office provide are labelled 1-6 below.

A. For the company folder, please create a front and back insert x 3 that is staggered (see pamphlet idea, sunday; and small-medium-large, Monday) and inserted on the right side. Our referral form that has been designed and will be included on the left (referral BCC Monday). Feel free to use the same themes.
Inserts in folder:
• 1. Echocardiogram and 2. Stress Echocardiogram (largest page front and back)
• 3. Holter/Loop monitor and 4. Ambulatory blood pressure monitoring (medium sized page front and back)
• 5. Electrocardiogram and 6. Cardiac Consultations (smallest page front and back)

In terms of content for the folder inserts, our word content will likely not be more than 2 or 3 sentences (we are drafting them now). Please ensure colorful and attractive graphics are used to highlight these tests. Please use, where possible, pictures of tests more than of people. The goal is to emphasize the role of the office as a testing center. Feel free to look them up online (eg. Echo, stress echo, Holter monitoring etc).

B. For the accordian Z fold brochure, please design it such where by each item we offer (from 1-6 below) occupy 1 page of fold, with the exception where item 5 - 6 combined into 1 page. The front page of course will be the office logo and address etc.

C. For the Large pull up poster display for BRAMLEY CARDIAC CENTRE - simple, with picture. Dimensions 33" x 81"
This banner will have our logo, and a summary of ll the services we provide (1 - 6)

Items need to be graphics heavy and attractive as we are trying to avoid making it wordy.

Target Market(s)

Referring physicians, patietns

Industry/Entity Type

Health Care

Requirements
Must have
• Attractive graphics and pictures.
• Most graphics emphasize diagnostic testing we do.
Should not have
• Too much word content

```html
<!DOCTYPE html>
<html lang="en">
<head>
<meta charset="utf-8">
<title>Bramley Cardiac Centre – Pull-up Banner</title>
<link rel="stylesheet" href="https://fonts.googleapis.com/css2?family=Roboto+Condensed:wght@400;700&family=Lato:wght@700&display=swap">
<style>
  :root {
    --stage: #e9eaec;
    --navy: #1d3461;
    --red: #c41e2e;
    --red-deep: #a8192a;
    --blue: #2a9fd0;
    --bullet: #4fc3f0;
    --pale: #f3efe9;
    --white: #ffffff;
    --scan-dark: #0f2447;
    --scan-mid: #23508f;
    --scan-glow: #b3323d;
  }
  * { margin: 0; padding: 0; box-sizing: border-box; }
  html, body {
    width: 1200px; height: 967px; overflow: hidden;
    background: var(--stage);
  }
  .banner {
    position: absolute;
    left: 410px; top: 18px;
    width: 380px; height: 930px;
    background: var(--white);
    box-shadow: 0 6px 24px rgba(0,0,0,.18);
    overflow: hidden;
  }
  .banner-shapes { position: absolute; inset: 0; }
  .brand {
    position: absolute; top: 28px; left: 0; right: 0;
    text-align: center;
    font-family: "Roboto Condensed", sans-serif;
    font-weight: 700;
    color: var(--navy);
  }
  .brand-mark {
    width: 34px; height: 34px; border-radius: 50%;
    background: var(--red);
    margin: 0 auto 8px;
  }
  .brand-name { font-size: 32px; line-height: 1; letter-spacing: 1px; }
  .brand-sub { font-size: 22px; line-height: 1.1; letter-spacing: 2px; }
  .services {
    position: absolute; left: 70px; top: 535px; right: 20px;
    list-style: none;
    font-family: "Roboto Condensed", sans-serif;
    font-size: 23px; line-height: 21px;
    color: var(--white);
  }
  .services li { position: relative; margin-bottom: 27px; }
  .services li::before {
    content: ""; position: absolute;
    left: -19px; top: 6px;
    width: 9px; height: 9px; border-radius: 50%;
    background: var(--bullet);
  }
  .web-address {
    position: absolute; left: 0; right: 0; bottom: 0; height: 34px;
    background: var(--blue);
    color: var(--white);
    font-family: "Lato", sans-serif; font-weight: 700;
    font-size: 14px; letter-spacing: 3.5px;
    text-align: center; line-height: 34px;
  }
</style>
</head>
<body>
  <section class="banner">
    <svg class="banner-shapes" width="380" height="930" viewBox="0 0 380 930">
      <defs>
        <radialGradient id="scan-tones" cx="50%" cy="60%" r="70%">
          <stop offset="0" stop-color="var(--scan-glow)"/>
          <stop offset="0.35" stop-color="var(--scan-mid)"/>
          <stop offset="1" stop-color="var(--scan-dark)"/>
        </radialGradient>
      </defs>
      <polygon class="header-band" points="0,132 380,195 380,210 0,151" fill="var(--red)"/>
      <polygon class="header-line" points="0,151 380,210 380,214 0,155" fill="var(--blue)"/>
      <g role="img" aria-label="Illustration of a human torso with a glowing heart and an ECG trace on a blue grid">
        <polygon points="0,155 380,214 380,525 0,463" fill="url(#scan-tones)"/>
      </g>
      <polygon class="image-edge" points="0,463 380,525 380,533 0,470" fill="var(--blue)"/>
      <polygon class="services-panel" points="0,470 380,533 380,897 0,897" fill="var(--red)"/>
      <polygon class="base-panel" points="0,828 380,890 380,897 0,897" fill="var(--pale)"/>
      <polygon points="0,828 380,890 380,893 0,831" fill="var(--red-deep)"/>
    </svg>

    <header class="brand">
      <div class="brand-mark"></div>
      <div class="brand-name">BRAMLEY CARDIAC</div>
      <div class="brand-sub">CENTRE</div>
    </header>

    <ul class="services">
      <li>Echocardiogram</li>
      <li>Stress Echocardiogram</li>
      <li>Holter/Loop monitor</li>
      <li>Ambulatory blood pressure monitoring</li>
      <li>Electrocardiogram</li>
      <li>Cardiac Consultations</li>
    </ul>

    <footer class="web-address">www.bramleycardiac.org</footer>
  </section>
</body>
</html>
```